Home page in PSD needed for a Business Consultant website

We have been given the mandate to re-do the website: http://www.velorancourt.ca/

Deliverable: home page in PSD format in French language

Context: Luc Brodeur is a business strategist specializing in marketing, creativity, business development. He helps small and medium companies develop their business through creative marketing strategies.

Some websites we like for your inspiration:

http://www.tallgreenbirch.com.au/
http://www.pdadvisory.com.au/
http://holtadvisors.com.au/
http://www.brumilotq.com/fr

Target Market(s)

B2B: Companies looking on the web for a business consultant who can help them with marketing, business developement, printing needs.

Industry/Entity Type

Business

Requirements
Must have
• Call to action: "Simplifiez votre développement des affaires" (which means "Simplify your business development")
• List of services (main menu)
• Marketing
• Développement des affaires
• Créativité
• Scolaire
• Impression
• Top menu as follow:
• Accueil
• À propos
• Contact

```html
<!DOCTYPE html>
<html lang="fr">
<head>
<meta charset="utf-8">
<title>Velorancourt — Luc Brodeur</title>
<link href="https://fonts.googleapis.com/css2?family=PT+Sans:ital,wght@0,400;0,700;1,400;1,700&display=swap" rel="stylesheet">
<style>
  :root {
    --page-bg: #f2f2f2;
    --ink: #111111;
    --ink-soft: #34344a;
    --accent: #0a75c2;
    --rule: #a9a9a9;
    --forest-light: #b9e27a;
    --forest-mid: #5f9a2e;
    --forest-dark: #2f4a1c;
    --caption-bar: rgba(40, 45, 60, 0.55);
    --white: #ffffff;
  }
  * { margin: 0; padding: 0; box-sizing: border-box; }
  html, body { width: 1200px; height: 675px; overflow: hidden; background: var(--page-bg); }
  body { font-family: "PT Sans", Arial, sans-serif; position: relative; }

  .site-header { position: absolute; left: 190px; top: 56px; width: 822px; height: 44px; }
  .brand { position: absolute; left: 0; top: 6px; display: flex; align-items: center; gap: 7px;
           font-size: 20px; font-weight: 400; color: var(--ink); letter-spacing: 0.5px; }
  .brand-mark { width: 12px; height: 12px; background: var(--accent); border-radius: 50%; }

  .main-nav { position: absolute; top: 22px; left: 0; width: 100%; }
  .main-nav a { position: absolute; transform: translateX(-50%); font-size: 12px; font-style: italic;
                font-weight: 700; color: var(--ink-soft); text-decoration: none; text-transform: uppercase;
                white-space: nowrap; }
  .main-nav a.is-current { color: var(--accent); }

  .social { position: absolute; right: 0; top: 21px; display: flex; align-items: center; gap: 9px;
            font-size: 12px; font-style: italic; font-weight: 700; text-transform: uppercase; }
  .social .label { color: var(--ink); margin-right: 2px; white-space: nowrap; }
  .social .label span { color: var(--accent); }
  .social .dot { width: 11px; height: 11px; background: var(--ink-soft); border-radius: 2px; }
  .social .mail { font-style: normal; font-weight: 400; color: var(--ink-soft); font-size: 13px; }

  .hero { position: absolute; left: 190px; top: 106px; width: 822px; height: 259px;
          border-radius: 9px; overflow: hidden;
          background: radial-gradient(ellipse at 58% 18%, #fbffd8 0%, var(--forest-light) 18%, var(--forest-mid) 52%, var(--forest-dark) 100%); }
  .hero-btn { position: absolute; top: 107px; width: 45px; height: 45px; border: 2px solid var(--white);
              border-radius: 50%; color: var(--white); font-size: 12px; font-style: italic; font-weight: 700;
              display: flex; align-items: center; justify-content: center; }
  .hero-btn.prev { left: 13px; }
  .hero-btn.next { right: 13px; }
  .hero-caption { position: absolute; left: 0; bottom: 0; width: 100%; height: 33px; background: var(--caption-bar);
                  display: flex; align-items: center; justify-content: space-between; padding: 0 14px 0 10px; }
  .hero-caption h2 { color: var(--white); font-size: 21px; font-style: italic; font-weight: 400; text-transform: uppercase; white-space: nowrap; }
  .hero-dots { display: flex; gap: 5px; }
  .hero-dots i { width: 11px; height: 11px; border-radius: 50%; background: rgba(255,255,255,0.6); }
  .hero-dots i.active { background: var(--white); }

  .intro { position: absolute; left: 200px; top: 388px; text-transform: uppercase; font-style: italic; }
  .intro h1 { font-size: 41px; line-height: 34px; font-weight: 400; color: var(--ink); }
  .intro h1 .surname { color: var(--accent); }
  .intro .tagline { font-size: 41px; line-height: 34px; color: var(--ink-soft); white-space: nowrap; }

  .rule { position: absolute; left: 190px; width: 822px; height: 1px; background: var(--rule); }
  .rule.top { top: 477px; }
  .rule.bottom { top: 638px; }

  .body-copy { position: absolute; left: 200px; top: 480px; width: 805px; height: 156px; overflow: hidden;
               font-size: 16.6px; line-height: 25.8px; font-style: italic; text-transform: uppercase; color: var(--ink-soft); }
  .body-copy strong { font-weight: 400; color: var(--accent); }
</style>
</head>
<body>
  <header class="site-header">
    <div class="brand"><span class="brand-mark"></span>Velorancourt</div>
    <nav class="main-nav">
      <a class="is-current" href="#" style="left:238px">Accueil</a>
      <a href="#" style="left:334px">À propos</a>
      <a href="#" style="left:435px">Contact</a>
      <a href="#" style="left:550px">Services</a>
    </nav>
    <div class="social">
      <span class="label">Restez <span>connecté</span></span>
      <span class="dot" aria-label="Réseau social"></span>
      <span class="dot" aria-label="Réseau social"></span>
      <span class="mail">@</span>
    </div>
  </header>

  <section class="hero" role="img" aria-label="Forêt ensoleillée de grands arbres verts">
    <div class="hero-btn prev">PRÉC.</div>
    <div class="hero-btn next">SUIV.</div>
    <div class="hero-caption">
      <h2>Simplifiez votre développement des affaires</h2>
      <div class="hero-dots"><i class="active"></i><i></i><i></i><i></i><i></i></div>
    </div>
  </section>

  <section class="intro">
    <h1>Luc <span class="surname">Brodeur</span></h1>
    <p class="tagline">Un stratège d'affaires!</p>
  </section>

  <div class="rule top"></div>
  <p class="body-copy">Luc Brodeur accompagne les petites et moyennes entreprises dans leur croissance grâce à des stratégies de marketing créatives. Ses services&nbsp;: <strong>marketing</strong>, <strong>développement des affaires</strong>, <strong>créativité</strong>, <strong>scolaire</strong> et <strong>impression</strong>. Chaque mandat commence par une écoute attentive de vos besoins, suivie d'un plan clair et mesurable. Simplifiez votre développement des affaires avec un partenaire qui conjugue rigueur, imagination et résultats concrets.</p>
  <div class="rule bottom"></div>
</body>
</html>
```